VELINTA Promotions - Business Card Design Project

We are looking for a classy business cards for Promotion Company based in Toronto, Canada named Velinta Promotions.

Velinta Promotions has an idea and vision to set high standard, be EXCLUSIVE and attract a group of people that will follow us through events we promote (night clubs, brand promotions, music events, and sport events)

We want to present a high standards and classy image to the others...
Updates

Target Market(s)

male/female age 25-40 Target: business owners young entrepreneur - clubing industry - media industry - promotion industry - marketing media industry

Industry/Entity Type

Events

Requirements
Must have
• business cards should be classy, make people feel exclusive , make people react ..

```html
<!DOCTYPE html>
<html lang="en">
<head>
<meta charset="utf-8">
<title>Velinta Promotions – Business Cards</title>
<link rel="stylesheet" href="https://fonts.googleapis.com/css2?family=Questrial&family=Montserrat:wght@700&display=swap">
<style>
  :root {
    --page-bg: #ffffff;
    --card-light: #0a7fa3;
    --card-mid: #0a5f84;
    --card-dark: #073a58;
    --brand-cyan: #1fc6e8;
    --text-light: #eef6fa;
    --ornament: rgba(160, 215, 235, 0.16);
    --icon-tile: #5b8fc4;
    --label-ink: #111111;
    --shadow: rgba(0, 0, 0, 0.75);
  }
  * { box-sizing: border-box; margin: 0; padding: 0; }
  html, body {
    width: 1200px; height: 1200px; overflow: hidden;
    background: var(--page-bg);
  }
  .canvas { position: relative; width: 1200px; height: 1200px; }

  .card {
    position: absolute;
    left: 208px;
    width: 472px;
    height: 334px;
    background: linear-gradient(135deg, var(--card-light) 0%, var(--card-mid) 50%, var(--card-dark) 100%);
    box-shadow: 8px 8px 6px var(--shadow);
    overflow: hidden;
    font-family: "Questrial", sans-serif;
    color: var(--text-light);
  }
  .card--back { top: 270px; }
  .card--front { top: 667px; }

  .side-label {
    position: absolute;
    font-family: "Montserrat", sans-serif;
    font-weight: 700;
    font-size: 29px;
    letter-spacing: 2px;
    color: var(--label-ink);
  }
  .side-label--back { left: 721px; top: 450px; }
  .side-label--front { left: 728px; top: 779px; }

  .ornament {
    position: absolute;
    border-radius: 50%;
    background: radial-gradient(ellipse at center, var(--ornament) 0%, rgba(160,215,235,0) 72%);
  }

  .brand-name {
    position: absolute;
    color: var(--brand-cyan);
    white-space: nowrap;
    letter-spacing: 0.5px;
  }
  .card--back .brand-name { left: 14px; top: 24px; font-size: 19px; }
  .card--front .brand-name { left: 20px; top: 22px; font-size: 31px; }

  .holder {
    position: absolute;
    left: 135px; top: 132px; width: 172px;
    text-align: center;
  }
  .holder__name {
    font-size: 23px;
    letter-spacing: 2px;
    padding-bottom: 2px;
    border-bottom: 1px solid var(--text-light);
  }
  .holder__role { font-size: 13px; letter-spacing: 1px; margin-top: 4px; }

  .contact {
    position: absolute; left: 27px; top: 190px;
    list-style: none; font-size: 14.5px; letter-spacing: 1px; line-height: 18px;
  }

  .social { position: absolute; left: 27px; top: 270px; display: flex; gap: 5px; }
  .social__tile { width: 22px; height: 23px; border-radius: 3px; background: var(--icon-tile); }

  .services {
    position: absolute; left: 74px; top: 309px;
    font-size: 10.5px; letter-spacing: 0.6px; white-space: nowrap;
    display: flex; align-items: center; gap: 6px;
  }
  .services__dot { width: 5px; height: 5px; border-radius: 50%; background: var(--text-light); }
</style>
</head>
<body>
<main class="canvas">

  <section class="card card--back" aria-label="Business card, back side">
    <div class="ornament" style="left:328px;top:2px;width:140px;height:56px" role="img" aria-label="Faint floral swirl flourish"></div>
    <div class="ornament" style="left:340px;top:250px;width:128px;height:80px" role="img" aria-label="Faint floral swirl flourish"></div>
    <div class="ornament" style="left:8px;top:262px;width:132px;height:68px" role="img" aria-label="Faint floral swirl flourish"></div>

    <div class="brand-name">VELINTA Promotions</div>

    <div class="holder">
      <div class="holder__name">YOUR NAME</div>
      <div class="holder__role">Position</div>
    </div>

    <ul class="contact">
      <li>Address:</li>
      <li>Office:</li>
      <li>Telp:</li>
      <li>Email:</li>
    </ul>

    <div class="social" aria-label="Social profiles">
      <span class="social__tile"></span>
      <span class="social__tile"></span>
    </div>

    <div class="services">
      <span>Night Clubs</span><span class="services__dot"></span>
      <span>Brand Promotions</span><span class="services__dot"></span>
      <span>Music Events</span><span class="services__dot"></span>
      <span>Sport Events</span>
    </div>
  </section>
  <div class="side-label side-label--back">Back</div>

  <section class="card card--front" aria-label="Business card, front side">
    <div class="ornament" style="left:324px;top:5px;width:140px;height:52px" role="img" aria-label="Faint floral swirl flourish"></div>
    <div class="ornament" style="left:4px;top:250px;width:128px;height:80px" role="img" aria-label="Faint floral swirl flourish"></div>
    <div class="ornament" style="left:338px;top:245px;width:130px;height:80px" role="img" aria-label="Faint floral swirl flourish"></div>

    <div class="brand-name">VELINTA Promotions</div>
  </section>
  <div class="side-label side-label--front">Front</div>

</main>
</body>
</html>
```